Velvet Lantern rebranding my business with a new business card

I have my new logo and now I need a refresher on my business cards. I really want something fun and fresh. I like black background or anything to make the color pop.
Logo
Name: Velvet Lantern
Contact Info as stated below:
Mara Pelkin
519-555-0147
Logo
Name: Velvet Lantern
Mara Pelkin
519-555-0147
fb.me/VelvetLanternbyMara
Instagram: @VelvetLanternbyMara

Industry/Entity Type

Business

Contact Information for Business Card

double-sided. Logo on one side. Contact info on the other.

Requirements
Must have
• Logo
• Name: Velvet Lantern
• Contact Info as stated below:
• Mara Pelkin
• 519-555-0147
• fb.me/VelvetLanternbyMara
• fb.me/VelvetLanternbyMara

```html
<!DOCTYPE html>
<html lang="en">
<head>
<meta charset="utf-8">
<title>Velvet Lantern — Business Card</title>
<link href="https://fonts.googleapis.com/css2?family=Open+Sans:wght@300;400;600&display=swap" rel="stylesheet">
<style>
  :root {
    --backdrop: #262626;
    --card-dark: #1c1c1c;
    --card-dark-edge: #2a2a2a;
    --ink: #2b2b2b;
    --text-light: #e9e4e8;
    --rose: #d9a9c8;
    --rose-line: #cfa3bf;
    --muted: #9a8f98;
    --grad-pink: #cf7fbf;
    --grad-blush: #f1d3ea;
    --grad-cream: #f6f0c6;
    --grad-mint: #a9d9c6;
  }
  * { box-sizing: border-box; margin: 0; padding: 0; }
  html, body {
    width: 1200px; height: 1015px; overflow: hidden;
    background: var(--backdrop);
    font-family: "Open Sans", Arial, sans-serif;
  }
  .stage {
    position: relative; width: 1200px; height: 1015px;
    display: flex; flex-direction: column; align-items: center;
    justify-content: center; gap: 55px;
  }
  .card {
    position: relative; width: 700px; height: 400px;
    border-radius: 26px; overflow: hidden;
    box-shadow: 0 18px 40px rgba(0,0,0,.45);
  }
  .card-front {
    background: linear-gradient(120deg, var(--grad-pink) 0%, var(--grad-blush) 30%, var(--grad-cream) 58%, var(--grad-mint) 100%);
    display: flex; align-items: center; justify-content: center;
  }
  .brand-name {
    font-weight: 600; font-size: 40px; letter-spacing: 1px; color: var(--ink);
  }
  .card-back {
    background: linear-gradient(160deg, var(--card-dark-edge) 0%, var(--card-dark) 60%);
    color: var(--text-light);
  }
  .brand-badge {
    position: absolute; right: 60px; top: 40px;
    width: 170px; height: 170px; border-radius: 50%;
    border: 2px solid var(--rose-line);
    display: flex; align-items: center; justify-content: center; text-align: center;
  }
  .brand-badge .brand-name {
    color: var(--rose); font-size: 24px; line-height: 1.2;
  }
  .person-name {
    position: absolute; left: 50px; top: 252px;
    font-weight: 300; font-size: 34px; color: var(--text-light);
  }
  .divider {
    position: absolute; left: 50px; right: 40px; top: 306px;
    height: 2px; background: var(--rose-line);
  }
  .contact-row {
    position: absolute; left: 50px; right: 40px; top: 322px;
    display: flex; align-items: center; gap: 10px;
    font-size: 15px; font-weight: 400; color: var(--text-light);
    white-space: nowrap;
  }
  .contact-item { display: flex; align-items: center; gap: 7px; }
  .contact-sep { color: var(--muted); }
  .icon { width: 14px; height: 14px; flex: none; }
  .icon-square { width: 13px; height: 13px; background: var(--rose); border-radius: 2px; flex: none; }
</style>
</head>
<body>
<main class="stage">
  <section class="card card-front" aria-label="Card front">
    <span class="brand-name">Velvet Lantern</span>
  </section>

  <section class="card card-back" aria-label="Card back">
    <div class="brand-badge"><span class="brand-name">Velvet<br>Lantern</span></div>
    <p class="person-name">Mara Pelkin</p>
    <div class="divider"></div>
    <div class="contact-row">
      <span class="contact-item">
        <svg class="icon" viewBox="0 0 16 16" aria-hidden="true"><path fill="var(--rose)" d="M3 1h3l1.5 4-2 1.3a9 9 0 0 0 4.2 4.2L11 8.5l4 1.5v3a2 2 0 0 1-2 2A12 12 0 0 1 1 3a2 2 0 0 1 2-2z"/></svg>
        519-555-0147
      </span>
      <span class="contact-sep">|</span>
      <span class="contact-item">
        <span class="icon-square" aria-hidden="true"></span>
        fb.me/VelvetLanternbyMara
      </span>
      <span class="contact-sep">|</span>
      <span class="contact-item">
        <svg class="icon" viewBox="0 0 16 16" aria-hidden="true"><rect x="1" y="3" width="14" height="10" rx="1" fill="var(--rose)"/><path d="M1.5 3.5 8 9l6.5-5.5" fill="none" stroke="var(--card-dark)" stroke-width="1.4"/></svg>
        mara@velvetlantern.ca
      </span>
    </div>
  </section>
</main>
</body>
</html>
```